HALVERWOOD MARKSMAN SPORTS, A modern indoor gun range comfortable for anyone to visit.

Please note the attached "Operating Plan", and "Letter of Introduction" for more details on our operation.

What we are looking for is the overall feel and look of the website. A lot of the details in how many links, what links, etc we will have built later. It's more important we get the right color scheme, flow, feel, etc.

This is an indoor gun range in Colorado. We are looking to be the skyline putt of the gun industry. We want a website that is simple, but stylish. Our range is forward thinking and modern. Please see our logo attached.

Our indoor range will also have a small cafe that will sell coffee, mixed soda drinks, and made from scratch cinnamon rolls.

Our look will be lighter colors. We want to avoid anything that would seem aggressive. Simple is the key here. We love simple clean designs. Pixel harbor has a good look and feel to it. Something with the same feel would be great. Our logo is red and black; however, we don't want the website to be dominated by those colors. Blue is also a great color.

We need a landing page that can shrink to different sizes of screens.
No mobile format.
Contact page with email submission
Menu will only have a couple links. We are open to different formats. Skyline putts format is also a good design.

Possible links will include: Home, Membership, About Us, Contact Us, Classes, Cafe

Target Market(s)

Primary target is male 35-55 years old with some college or more.

Number of Pages Required

3 page

Font styles to use
Sans Serif

Colors

Designer to choose colors to be used in the design.

Requirements
Must have
• Page 1 Landing first page
• Page 2 Blog posts to give updates on building progress
• Page 3 About us (hours of operation, etc)

```html
<!DOCTYPE html>
<html lang="en">
<head>
<meta charset="utf-8">
<title>Halverwood Marksman Sports</title>
<link href="https://fonts.googleapis.com/css2?family=Montserrat:wght@400;500;600;700;800&family=Open+Sans:wght@400;600&display=swap" rel="stylesheet">
<style>
  :root {
    --red: #cc0000;
    --ink: #1c1c1c;
    --text: #444444;
    --band: #e5e5e5;
    --cell-dark: #d7d7d7;
    --cell-light: #e4e4e4;
    --footer: #1e1e1e;
    --white: #ffffff;
  }
  * { box-sizing: border-box; margin: 0; padding: 0; }
  html, body { width: 1200px; height: 4087px; overflow: hidden; background: var(--white); }
  body { font-family: "Open Sans", Arial, sans-serif; color: var(--text); }
  .page { position: relative; width: 1200px; height: 4087px; overflow: hidden; }
  .abs { position: absolute; }
  .heading { font-family: "Montserrat", Arial, sans-serif; font-weight: 800; color: var(--ink); text-transform: uppercase; letter-spacing: 0; }
  .body-copy { font-size: 15px; line-height: 29px; color: var(--text); }
  .text-block { position: absolute; display: flex; flex-direction: column; align-items: flex-start; }
  .btn { background: var(--red); color: var(--white); font-family: "Montserrat", Arial, sans-serif; font-weight: 700; font-size: 13px; display: flex; align-items: center; justify-content: center; text-transform: uppercase; width: 111px; height: 35px; }

  /* header */
  .brand { left: 144px; top: 24px; display: flex; align-items: center; gap: 12px; }
  .brand-mark { width: 40px; height: 40px; border: 3px solid var(--red); border-radius: 50%; }
  .brand-name { font-family: "Montserrat", Arial, sans-serif; font-weight: 800; font-size: 17px; line-height: 19px; color: var(--ink); }
  .social { top: 24px; width: 40px; height: 40px; border: 1.5px solid #b9b9b9; border-radius: 50%; }
  .nav { top: 85px; right: 145px; display: flex; gap: 33px; font-family: "Montserrat", Arial, sans-serif; font-size: 13px; color: #333; }
  .nav .active { color: var(--red); }

  /* hero */
  .hero { left: 0; top: 122px; width: 1200px; height: 572px; background: linear-gradient(100deg, #5d7189 0%, #3d4a58 30%, #22272d 55%, #141618 100%); clip-path: polygon(0 0, 100% 0, 100% 494px, 0 572px); }
  .hero-title { right: 145px; top: 306px; text-align: right; font-family: "Montserrat", Arial, sans-serif; font-weight: 800; font-size: 33px; line-height: 36px; color: var(--white); text-transform: uppercase; }
  .hero-btn { left: 927px; top: 389px; width: 128px; height: 33px; background: var(--white); color: var(--red); font-family: "Montserrat", Arial, sans-serif; font-weight: 700; font-size: 12.5px; display: flex; align-items: center; justify-content: center; }
  .hero-arrow { top: 349px; width: 40px; height: 40px; border-radius: 50%; background: rgba(255,255,255,0.9); display: flex; align-items: center; justify-content: center; }

  .photo { position: absolute; }
  .photo-shadow { position: absolute; background: #2a2a2a; }
  .band { left: 0; width: 1200px; background: var(--band); }

  /* pricing */
  .center { left: 0; width: 1200px; text-align: center; }
  .red-sub { font-family: "Montserrat", Arial, sans-serif; font-size: 27px; color: var(--red); }
  .fee-card { top: 1955px; height: 129px; background: var(--band); border-bottom: 3px solid var(--red); text-align: center; font-family: "Montserrat", Arial, sans-serif; }
  .fee-price { margin-top: 18px; font-weight: 800; font-size: 44px; color: var(--red); line-height: 52px; }
  .fee-label { font-size: 15.5px; color: #222; }
  .fee-note { font-size: 9px; color: #222; margin-top: 6px; }
  .initial { left: 144px; top: 2192px; width: 911px; height: 62px; background: var(--band); display: flex; align-items: center; justify-content: center; font-family: "Montserrat", Arial, sans-serif; font-size: 24px; color: #222; }
  .initial b { color: var(--red); font-weight: 500; margin-right: 6px; }

  .plan { left: 144px; width: 911px; font-family: "Montserrat", Arial, sans-serif; }
  .plan-head { height: 47px; background: var(--ink); color: var(--white); display: flex; align-items: center; padding-left: 24px; font-weight: 700; font-size: 23px; }
  .plan-head small { font-size: 9px; font-weight: 400; margin-left: 12px; margin-top: 3px; }
  .plan-row { display: flex; height: 39px; margin-top: 3px; font-size: 16.5px; }
  .plan-row .tier { width: 207px; background: var(--cell-dark); padding-left: 24px; display: flex; align-items: center; color: #222; }
  .plan-row .rate { flex: 1; background: var(--cell-light); padding-left: 24px; display: flex; align-items: center; color: var(--red); }
  .plan-row .rate small { font-size: 9.5px; color: #222; margin-left: 9px; }
  .plan-foot { left: 144px; top: 2639px; width: 911px; height: 37px; background: var(--red); color: var(--white); font-family: "Montserrat", Arial, sans-serif; font-weight: 700; font-size: 15px; display: flex; align-items: center; justify-content: center; }

  /* contact */
  .contact-box { left: 144px; top: 3510px; width: 911px; height: 320px; background: var(--band); }
  .map { left: 144px; top: 3510px; width: 456px; height: 320px; background: linear-gradient(135deg, #d9d9d9, #c6c6c6 60%, #d4d4d4); }
  .info { left: 638px; font-family: "Montserrat", Arial, sans-serif; font-size: 16px; color: #222; display: flex; gap: 10px; }
  .info svg { flex: none; margin-top: 3px; }
  .hours { left: 662px; top: 3691px; font-family: "Montserrat", Arial, sans-serif; font-size: 16px; line-height: 25.5px; color: #222; }
  .hours small { display: block; font-size: 10px; line-height: 16px; margin-top: 8px; }

  /* footer */
  .footer { left: 0; top: 3900px; width: 1200px; height: 187px; background: var(--footer); clip-path: polygon(0 82px, 100% 19px, 100% 100%, 0 100%); }
  .footer-links { left: 144px; top: 3988px; font-size: 11.5px; color: #9a9a9a; }
  .footer-links span { margin: 0 8px; }
  .copyright { left: 144px; top: 4036px; font-size: 11.5px; color: #9a9a9a; }
  .to-top { left: 1014px; top: 4005px; width: 40px; height: 40px; border-radius: 50%; background: #555; display: flex; align-items: center; justify-content: center; }
</style>
</head>
<body>
<div class="page">

  <!-- header -->
  <div class="abs brand">
    <div class="brand-mark"></div>
    <div class="brand-name">HALVERWOOD<br>MARKSMAN SPORTS</div>
  </div>
  <div class="abs social" style="left:902px"></div>
  <div class="abs social" style="left:959px"></div>
  <div class="abs social" style="left:1015px"></div>
  <nav class="abs nav">
    <span class="active">HOME</span><span>MEMBERSHIP</span><span>ABOUT US</span><span>CONTACT US</span><span>CLASSES</span><span>CAFE</span>
  </nav>

  <!-- hero -->
  <div class="abs hero" role="img" aria-label="Photo of a shooter wearing ear protection aiming a rifle in an indoor range"></div>
  <div class="abs hero-title">Colorado’s Finest<br>Indoor Shooting Range</div>
  <div class="abs hero-btn">VIEW CLASSES</div>
  <div class="abs hero-arrow" style="left:55px">
    <svg width="14" height="14" viewBox="0 0 14 14"><path d="M9 2 L4 7 L9 12" fill="none" stroke="#222" stroke-width="2.5"/></svg>
  </div>
  <div class="abs hero-arrow" style="left:1102px">
    <svg width="14" height="14" viewBox="0 0 14 14"><path d="M5 2 L10 7 L5 12" fill="none" stroke="#222" stroke-width="2.5"/></svg>
  </div>

  <!-- welcome -->
  <div class="text-block" style="left:144px;top:768px;width:535px">
    <h1 class="heading" style="font-size:28px;line-height:36px">Welcome to<br>Halverwood Marksman Sports</h1>
    <p class="body-copy" style="margin-top:8px">We plan to start a family run state of the art indoor shooting range that is safe.&nbsp; We will foster an environment that allows men and women to come by themselves, feel comfortable, and are confident regardless of their experience level. We will hire staff based on guest service skills to focus on their overall experience.</p>
    <div class="btn" style="margin-top:14px">Read More</div>
  </div>
  <div class="photo-shadow" style="left:714px;top:783px;width:341px;height:269px"></div>
  <div class="photo" role="img" aria-label="Photo of rifles standing in a display rack" style="left:706px;top:775px;width:341px;height:269px;background:linear-gradient(120deg,#2b2b2b,#5a4a42 45%,#8a5a3c 75%,#c7a88a)"></div>

  <!-- services -->
  <div class="abs band" style="top:1132px;height:615px;clip-path:polygon(0 82px,100% 0,100% 538px,0 615px)"></div>
  <div class="photo-shadow" style="left:144px;top:1301px;width:342px;height:288px"></div>
  <div class="photo" role="img" aria-label="Photo of a man with ear protection aiming a handgun at a paper target" style="left:152px;top:1293px;width:342px;height:288px;background:linear-gradient(90deg,#8b8f8a,#b9bbb5 40%,#6f6a62 70%,#4a4440)"></div>
  <div class="text-block" style="left:524px;top:1287px;width:535px">
    <h2 class="heading" style="font-size:31px;line-height:38px">Our Services</h2>
    <p class="body-copy" style="margin-top:6px">Halverwood Marksman Sports will have 22 individual room lanes: 5 lanes at 25 yard range, 13 lanes at 10 yard ranges, and 4 lanes at 5 yard range dedicated to an advanced live fire interactive graphic experience. We will also have a 22 foot wide open range for classes, corporate events, groups, and special training. There will be a 2,000 square foot retail area, small gunsmith corner, 2 classrooms that double as event rooms, dedicated range safety officer monitoring room, and small café.</p>
    <div class="btn" style="margin-top:14px">Read More</div>
  </div>

  <!-- pricing -->
  <h2 class="abs heading center" style="top:1822px;font-size:31px">Our Pricing</h2>
  <p class="abs center" style="top:1882px;font-family:'Montserrat',Arial,sans-serif;font-size:19px;color:#222">All lanes are first come first serve. The only reservations will be for founding members.</p>
  <p class="abs center red-sub" style="top:1911px">Fees:</p>
  <div class="abs fee-card" style="left:144px;width:297px">
    <div class="fee-price">$20</div><div class="fee-label">Lane Rental per day</div><div class="fee-note">(no extra cost for additional people in 1 lane)</div>
  </div>
  <div class="abs fee-card" style="left:452px;width:296px">
    <div class="fee-price">$20</div><div class="fee-label">Unlimited gun rentals</div>
  </div>
  <div class="abs fee-card" style="left:759px;width:296px">
    <div class="fee-price">$10</div><div class="fee-label">Single gun rental</div>
  </div>
  <p class="abs center red-sub" style="top:2142px">Memberships will be offered:</p>
  <div class="abs initial"><b>$58</b> Initial Fee (Waived if signed up prior to opening)</div>

  <div class="abs plan" style="top:2272px">
    <div class="plan-head">YEARLY</div>
    <div class="plan-row"><div class="tier">Individual</div><div class="rate">$300 a year</div></div>
    <div class="plan-row"><div class="tier">Dual</div><div class="rate">$400 a year</div></div>
    <div class="plan-row"><div class="tier">Family</div><div class="rate">$450 a year<small>(Children are included up to age 26, and they do not need to live at home)</small></div></div>
  </div>
  <div class="abs plan" style="top:2463px">
    <div class="plan-head">MONTH-MONTH<small>(no contract or obligation)</small></div>
    <div class="plan-row"><div class="tier">Individual</div><div class="rate">$30 a month</div></div>
    <div class="plan-row"><div class="tier">Dual</div><div class="rate">$40 a month</div></div>
    <div class="plan-row"><div class="tier">Family</div><div class="rate">$45 a month<small>(Children age up to 26, and they do not need to live at home)</small></div></div>
  </div>
  <div class="abs plan-foot">MEMBERS ARE ALLOWED UNLIMITED VISITS TO THE RANGE</div>

  <!-- cafe -->
  <div class="abs band" style="top:2757px;height:615px;clip-path:polygon(0 79px,100% 0,100% 536px,0 615px)"></div>
  <div class="text-block" style="left:144px;top:2910px;width:535px">
    <h2 class="heading" style="font-size:31px;line-height:38px">Café</h2>
    <p class="body-copy" style="margin-top:6px">Café will sell a small variety of coffee and mixed soda drinks. It will also carry made from scratch cinnamon rolls sold on a first come basis until sold out daily.</p>
    <p class="body-copy" style="margin-top:29px">Maecenas consequat justo enim, ac mattis massa imperdiet quis. Fusce eget neque elit. Sed augue orci, elementum in magna congue, tincidunt vulputate erat. Aliquam consectetur orci molestie dictum molestie.</p>
    <div class="btn" style="margin-top:14px">Read More</div>
  </div>
  <div class="photo-shadow" style="left:714px;top:2928px;width:341px;height:286px"></div>
  <div class="photo" role="img" aria-label="Photo of a cup of coffee on a wooden café table" style="left:706px;top:2920px;width:341px;height:286px;background:linear-gradient(160deg,#6b4a35,#a77d5a 40%,#4a2e1e 75%,#2c1a10)"></div>

  <!-- contact -->
  <h2 class="abs heading center" style="top:3455px;font-size:31px">Contact Info</h2>
  <div class="abs contact-box"></div>
  <div class="abs map" role="img" aria-label="Street map showing the range location"></div>
  <div class="abs info" style="top:3549px">
    <svg width="12" height="14" viewBox="0 0 12 14"><path d="M6 0a5 5 0 0 0-5 5c0 4 5 9 5 9s5-5 5-9a5 5 0 0 0-5-5zm0 7a2 2 0 1 1 0-4 2 2 0 0 1 0 4z" fill="#333"/></svg>
    <span>24 Building name, Street name, City Zipcode</span>
  </div>
  <div class="abs info" style="top:3589px">
    <svg width="12" height="14" viewBox="0 0 12 12"><path d="M2.5 0.5l2 2.5-1 1.5c.8 1.6 2 2.8 3.5 3.5l1.5-1 2.5 2-1 2C5.5 11 1 6.5.5 2z" fill="#333"/></svg>
    <span>Phone : 555 014 2290</span>
  </div>
  <div class="abs info" style="top:3629px">
    <svg width="12" height="14" viewBox="0 0 12 10"><rect x="0" y="1" width="12" height="9" fill="#333"/><path d="M0 1 L6 6 L12 1" fill="none" stroke="#e5e5e5" stroke-width="1.2"/></svg>
    <span>Email : hello@halverwoodrange.com</span>
  </div>
  <div class="abs info" style="top:3668px">
    <svg width="12" height="14" viewBox="0 0 12 12"><circle cx="6" cy="6" r="5" fill="none" stroke="#333" stroke-width="1.5"/><path d="M6 3v3.5h2.5" fill="none" stroke="#333" stroke-width="1.3"/></svg>
    <span>Our open hours will be:</span>
  </div>
  <div class="abs hours">
    Monday – Thursday: 10am to 8pm<br>
    Friday &amp; Saturday: 9 am to 10pm<br>
    Sunday: CLOSED
    <small>First Wednesday of every month we will open at 6 am and close regularly.</small>
  </div>

  <!-- footer -->
  <div class="abs footer"></div>
  <div class="abs footer-links">Home<span>|</span>Membership<span>|</span>About Us<span>|</span>Contact Us<span>|</span>Classes<span>|</span>Cafe</div>
  <div class="abs copyright">Copyright © 2019 &nbsp;Halverwood Marksman Sports. &nbsp;All rights reserved.</div>
  <div class="abs to-top">
    <svg width="18" height="12" viewBox="0 0 18 12"><path d="M2 10 L9 3 L16 10" fill="none" stroke="#1e1e1e" stroke-width="3"/></svg>
  </div>
</div>
</body>
</html>
```